Adventurous female pilot

I am looking for a personal business card, for a very well qualified female pilot, with a lot of aviation experience.

Currently an airline pilot, have worked as a bush pilot in Africa, looking to get into corporate aviation, or private jet owners.
Want a classy looking card for networking...

Could be interested in a retro\vintage look also?!

An idea,, is an african sunset background, with my wings\logo on it
Updates

I just want to say thank you to all of your for your amazing designs!

I have been very busy flying this past week , so not had a chance to be on the computer much.
But I provide some feedback, and conclusions very soon!
Thank you again.

Marla

Reason: Still waiting on a couple of revisions to be 100% about my choice!

Target Market(s)

corporate aviation, private jet owners, casino's,
General audience.
networking

Industry/Entity Type

Airline

Requirements
Nice to have
• Classy, edgy, sexy, but also feminine

```html
<!DOCTYPE html>
<html lang="en">
<head>
<meta charset="utf-8">
<title>Marla Vance Aviation – Business Card</title>
<link rel="stylesheet" href="https://fonts.googleapis.com/css2?family=Jost:wght@300;400&family=Roboto+Condensed:wght@400&display=swap">
<style>
  :root {
    --stage: #242428;
    --card-front: #ffffff;
    --card-back: #050607;
    --ink-light: #ffffff;
    --mark-grey: #9a9a9c;
    --divider: rgba(255,255,255,0.55);
  }
  * { margin: 0; padding: 0; box-sizing: border-box; }
  html, body {
    width: 1200px; height: 1200px; overflow: hidden;
    background: var(--stage);
  }
  .stage { position: relative; width: 1200px; height: 1200px; }
  .card {
    position: absolute; top: 440px;
    width: 534px; height: 320px;
  }
  .card--front { left: 47px; background: var(--card-front); }
  .card--back { left: 619px; background: var(--card-back); color: var(--ink-light); }

  .brand-mark {
    position: absolute; left: 0; right: 0; top: 138px;
    text-align: center;
    font-family: "Jost", sans-serif; font-weight: 300;
    font-size: 30px; letter-spacing: 0.18em;
    color: var(--mark-grey);
  }

  .identity {
    position: absolute; left: 0; right: 0; top: 135px;
    text-align: center;
    font-family: "Jost", sans-serif; font-weight: 300;
    line-height: 1;
  }
  .identity__name { font-size: 27px; letter-spacing: 0.03em; }
  .identity__role { font-size: 19px; letter-spacing: 0.05em; margin-top: 6px; padding-left: 16px; }

  .contact {
    position: absolute; top: 264px;
    font-family: "Roboto Condensed", sans-serif;
    font-size: 13px; line-height: 17px;
  }
  .contact--address { left: 39px; }
  .contact--address .spaced { letter-spacing: 0.42em; }
  .contact--phone { left: 229px; width: 100px; text-align: center; }
  .contact--phone .landline { letter-spacing: 0.08em; }
  .contact--web { right: 39px; text-align: right; }

  .divider {
    position: absolute; top: 256px; width: 1px; height: 46px;
    background: linear-gradient(to bottom, transparent, var(--divider), transparent);
  }
  .divider--one { left: 211px; }
  .divider--two { left: 352px; }
</style>
</head>
<body>
<main class="stage">
  <section class="card card--front" aria-label="Card front">
    <div class="brand-mark">MARLA VANCE</div>
  </section>

  <section class="card card--back" aria-label="Card back">
    <div class="identity">
      <div class="identity__name">MARLA VANCE</div>
      <div class="identity__role">AVIATION</div>
    </div>

    <div class="contact contact--address">
      <div class="spaced">dummy dummy</div>
      <div>dummy dummy City dummy</div>
    </div>
    <span class="divider divider--one"></span>
    <div class="contact contact--phone">
      <div>+63 900 5550142</div>
      <div class="landline">(083) 555014</div>
    </div>
    <span class="divider divider--two"></span>
    <div class="contact contact--web">
      <div>john@marlavance.com</div>
      <div>www.marlavance.com</div>
    </div>
  </section>
</main>
</body>
</html>
```